TRENDY & MODERN BUSINESS CARD DESIGN for Media Company *

I need a minimalistic - clean - modern and professional business card layout and design for MEDIA & PHOTOGRAPHY STUDIO.

We do NOT have a logo, and not really looking for one - but rather excellent typography and design. We would consider the 3 as a focal point.

We do personal and commercial photography.

Target Market(s)

Personal and commercial photography clientele

Contact Information for Business Card

ZUB size - from zub.com / size guidelines are enclosed in the brief

Font styles to use
Sans Serif

Colors
f78f20
eda3c7
cee9f5
0555a3
e667a6
fbf289

Requirements
Must have
• Clean lines - Modern layout
Nice to have
• All blue background as an option - use color palette in brief please.
Should not have
• Old fashion fonts and regular fonts.

```html
<!DOCTYPE html>
<html lang="en">
<head>
<meta charset="utf-8">
<title>Prism Lane Media – Business Card</title>
<link rel="stylesheet" href="https://fonts.googleapis.com/css2?family=Open+Sans:wght@400;600;700&family=Satisfy&display=swap">
<style>
  :root {
    --backdrop: #7a7a7c;
    --card-white: #fbfbfb;
    --brand-blue: #2f4f9e;
    --back-blue-light: #3f62ad;
    --back-blue-dark: #22428c;
    --tile-yellow: #ebe382;
    --tile-pink: #d6a6c8;
    --tile-sky: #cfe2ec;
    --text-white: #ffffff;
  }
  * { box-sizing: border-box; margin: 0; padding: 0; }
  html, body {
    width: 1200px; height: 971px; overflow: hidden;
    background: var(--backdrop);
    font-family: "Open Sans", Arial, sans-serif;
  }
  .sheet { position: relative; width: 1200px; height: 971px; }
  .card {
    position: absolute; top: 331px; width: 540px; height: 309px;
    border-radius: 3px;
    box-shadow: 0 6px 18px rgba(0,0,0,.25);
    overflow: hidden;
  }
  /* Front */
  .card-front { left: 45px; background: var(--card-white); }
  .wordmark { position: absolute; top: 92px; left: 0; right: 0; text-align: center; }
  .wordmark-name {
    display: inline-block;
    font-weight: 600; font-size: 34px; letter-spacing: 1.5px;
    color: var(--brand-blue);
    padding: 0 6px 4px;
    border-bottom: 1.5px solid var(--brand-blue);
  }
  .tagline { margin-top: 6px; font-size: 12px; color: var(--brand-blue); letter-spacing: .3px; }
  .locations {
    position: absolute; bottom: 28px; left: 0; right: 0; text-align: center;
    font-size: 11px; letter-spacing: 2.2px; color: var(--brand-blue);
  }
  /* Back */
  .card-back {
    left: 615px;
    background: radial-gradient(ellipse at 40% 40%, var(--back-blue-light) 0%, var(--back-blue-dark) 100%);
    color: var(--text-white);
  }
  .holder { position: absolute; top: 40px; right: 34px; text-align: right; }
  .holder-name { font-family: "Satisfy", cursive; font-size: 34px; line-height: 1.1; }
  .holder-title { font-size: 10px; margin-top: 2px; }
  .contact-tiles { position: absolute; left: 58px; top: 128px; width: 30px; }
  .tile { height: 44px; display: flex; align-items: center; justify-content: center; }
  .tile-phone { background: var(--tile-yellow); }
  .tile-mail { background: var(--tile-pink); }
  .tile-pin { background: var(--tile-sky); height: 70px; }
  .contact-lines {
    position: absolute; left: 100px; top: 128px;
    font-size: 14px; line-height: 1.3;
  }
  .contact-line { height: 44px; display: flex; align-items: center; }
  .contact-address { height: 70px; display: flex; flex-direction: column; justify-content: center; }
</style>
</head>
<body>
<main class="sheet">
  <section class="card card-front" aria-label="Card front">
    <div class="wordmark">
      <div class="wordmark-name">PRISM LANE MEDIA</div>
      <div class="tagline">Framing Moments.&nbsp; Telling Stories.</div>
    </div>
    <div class="locations">Miami • New York • Las Vegas • Cancun</div>
  </section>

  <section class="card card-back" aria-label="Card back">
    <div class="holder">
      <div class="holder-name">Marisol Vega</div>
      <div class="holder-title">Founder &amp; Media Director</div>
    </div>
    <div class="contact-tiles">
      <div class="tile tile-phone">
        <svg width="16" height="16" viewBox="0 0 24 24" aria-hidden="true"><path fill="#fff" d="M6.6 10.8a15.1 15.1 0 0 0 6.6 6.6l2.2-2.2c.3-.3.7-.4 1-.2 1.1.4 2.3.6 3.6.6.6 0 1 .4 1 1V20c0 .6-.4 1-1 1A17 17 0 0 1 3 4c0-.6.4-1 1-1h3.5c.6 0 1 .4 1 1 0 1.3.2 2.5.6 3.6.1.3 0 .7-.2 1z"/></svg>
      </div>
      <div class="tile tile-mail">
        <svg width="18" height="14" viewBox="0 0 18 14" aria-hidden="true"><rect x="1" y="1" width="16" height="12" fill="none" stroke="#fff" stroke-width="1.5"/><path d="M1 1l8 7 8-7" fill="none" stroke="#fff" stroke-width="1.5"/></svg>
      </div>
      <div class="tile tile-pin">
        <svg width="14" height="20" viewBox="0 0 14 20" aria-hidden="true"><path d="M7 1a6 6 0 0 0-6 6c0 4.5 6 12 6 12s6-7.5 6-12a6 6 0 0 0-6-6z" fill="none" stroke="#fff" stroke-width="1.5"/><circle cx="7" cy="7" r="2" fill="#fff"/></svg>
      </div>
    </div>
    <div class="contact-lines">
      <div class="contact-line">(305) 555-0142</div>
      <div class="contact-line">mar@prismlanemedia.com</div>
      <div class="contact-address"><span>2400 Harbor Avenue</span><span>6th Floor</span><span>Miami, FL 33199</span></div>
    </div>
  </section>
</main>
</body>
</html>
```